Tanzeri Corporate Site Template/Blog Design

Company Info: Tanzeri Mechanics is a San Francisco based start-up and spin-off of Halvorsen Polytechnic Automation Institute. Our mission is to transform the consumer experience through personal robotics technology.

Our first public brand, gizmopals.net (GPN), used these technologies to develop engaging toy and gaming category innovations that enhance the way children play and interact with new technologies.

This assignment is about the Tanzeri Mechanic corporate identity and not about GPN

The company is transitioning to include higher end consumer electronics and personal robotics products lines within the next few years, and we would like to establish a more formal corporate identity. Attached please find a user flow of the design needed, as well as our current logo.

High Res .EPS Link below:

https://tzmech.filecrate.example/shared/static/a27c0e91bd3f45a6c0d1.eps

Design Vision: Tanzeri Mechanics is in search of a simple, clean and easily updateable corporate website with an integrated blog. The company's current public profile is primarily GPN with an emphasis our children's toy lines Wuzzit and Clankeroos. Although you should be aware of these toy sites, please do not let them influence your design. What we are looking for is more of a blend of scientific and cool.

We would like to see a site template and design that is clean and approachable. It also needs to be able to support a CMS platform as we need the ability to allow our marketing team to update and manage content as well as add additional features such as video and ecommerce in the future as the company grows. These designs should also work well with Chatterly and Peepwire.

Attached is an image of our corporate card. The current color scheme is very basic but the design should complement them.

The final design and layout should communicate a sleek, innovative and technologically saavy consumer electronics and personal robotics company. Again, we are a consumer oriented organization but the key audiences for this site will be investors, media, retail and biz dev partners, and potential employees

Target Market(s)

Investors, Biz dev and other partners, retail, Media, employees. Consumers secondary

Industry/Entity Type

Electronics

Requirements
Must have
• The site must have all of the tabs that we have identified in the attached user flow.

The design must be able to support a backend content management system. We currently have an upgraded PageLoft account, and can provide access if needed but will soon transition to our own site. we are open to your recommendations. Our objective is to be able to easily update the content without relying on a developer.

Font should be sleek. And not bubbly.
Nice to have
• Clean site design. Simple layouts. A blend between scientific and cool. Easy to navigate tabs and sub tabs. forward thinking imagery

Should not have
• Nothing complex on the Homepage- should be very simple. No cartoonish robots, bright colors. Little or no use of humans in stock photos. No competative products or copy. Toys should be under product tabs, and not featured on the homepage as in our initial design efforts we felt that the two were aesthetically polarizing. Just to confirm, the Tanzeri Corporate site should serve more as the parent site, and the toy lines should stay under the sub navs on the product page.

```html
<!DOCTYPE html>
<html lang="en">
<head>
<meta charset="utf-8">
<title>Tanzeri Mechanics — Home</title>
<link href="https://fonts.googleapis.com/css2?family=Open+Sans:wght@300;400;600;700;800&display=swap" rel="stylesheet">
<style>
  :root {
    --ink: #2e2e2e;
    --text: #333333;
    --accent: #1a7fc1;
    --band-light: #f4f4f4;
    --band-dark: #d2d2d2;
    --panel: #ffffff;
    --post-bg: #f7f7f7;
    --rule: #e4e4e4;
    --faint: #e6e6e6;
    --gold-light: #e8cf5a;
    --gold: #c9a22a;
    --gold-dark: #6b5418;
  }
  * { box-sizing: border-box; margin: 0; padding: 0; }
  html, body { width: 1200px; height: 771px; overflow: hidden; background: #fff; }
  body { font-family: "Open Sans", Arial, sans-serif; color: var(--text); position: relative; }

  .site-header { position: absolute; left: 0; top: 0; width: 1200px; height: 154px; }
  .brand {
    position: absolute; left: 178px; top: 52px;
    font-weight: 800; font-size: 34px; line-height: 1; letter-spacing: 1px;
    color: var(--ink); text-transform: uppercase;
  }
  .main-nav { position: absolute; right: 181px; top: 70px; display: flex; gap: 33px; }
  .main-nav a {
    font-size: 14px; font-weight: 600; color: var(--ink);
    text-decoration: none; text-transform: uppercase; letter-spacing: -0.2px;
  }
  .main-nav a.is-active { color: var(--accent); }

  .feature-band {
    position: absolute; left: 0; top: 154px; width: 1200px; height: 421px;
    background:
      radial-gradient(ellipse 45% 60% at 50% 45%, var(--band-light) 0%, rgba(244,244,244,0) 100%),
      linear-gradient(180deg, #e2e2e2 0%, #ededed 40%, var(--band-dark) 100%);
  }
  .feature-panel {
    position: absolute; left: 179px; top: 31px; width: 840px; height: 359px;
    background: var(--panel); box-shadow: 0 3px 8px rgba(0,0,0,0.18);
    display: flex;
  }
  .news { width: 420px; height: 359px; display: flex; flex-direction: column; border-right: 1px solid var(--rule); }
  .news-title {
    height: 75px; padding: 16px 0 0 32px;
    font-weight: 300; font-size: 40px; line-height: 1.1; color: var(--ink);
    border-bottom: 1px solid var(--rule);
  }
  .post-head {
    height: 27px; display: flex; justify-content: space-between; align-items: center;
    padding: 0 17px 0 33px; border-bottom: 1px solid var(--rule); background: #fff;
  }
  .post-title { font-size: 14px; font-weight: 700; color: var(--ink); }
  .post-date { font-size: 9.5px; font-weight: 700; color: var(--ink); }
  .post-body {
    background: var(--post-bg); padding: 12px 22px 0 33px; height: 101px;
    font-size: 11px; line-height: 17px; color: var(--text);
  }
  .post-body.is-last { height: 100px; border-bottom: 1px solid var(--rule); }
  .read-more { font-size: 8.5px; font-weight: 600; color: var(--ink); text-transform: uppercase; margin-left: 3px; }
  .read-more a { color: var(--ink); }
  .archive-link {
    flex: 1; display: flex; justify-content: flex-end; align-items: center; padding-right: 17px;
    font-size: 9.5px; font-weight: 700; text-transform: uppercase; color: var(--ink); text-decoration: none;
  }
  .feature-art { width: 420px; height: 359px; display: block; }

  .site-footer { position: absolute; left: 0; top: 575px; width: 1200px; height: 196px; }
  .contact-block {
    position: absolute; left: 178px; top: 23px;
    font-size: 11px; line-height: 15.5px; color: var(--text);
  }
  .contact-block p + p { margin-top: 8px; }
  .contact-block strong { font-weight: 700; }
  .contact-block a { color: var(--text); }
  .footer-brand {
    position: absolute; left: 446px; top: 74px; width: 308px; text-align: center;
    font-weight: 800; font-size: 30px; line-height: 1; color: var(--faint); text-transform: uppercase;
  }
  .copyright {
    position: absolute; right: 180px; top: 23px; text-align: right;
    font-size: 11px; line-height: 15.5px; color: var(--text);
  }
</style>
</head>
<body>
  <header class="site-header">
    <div class="brand">Tanzeri Mechanics</div>
    <nav class="main-nav">
      <a href="#" class="is-active">Home</a>
      <a href="#">About Us</a>
      <a href="#">Products</a>
      <a href="#">News</a>
      <a href="#">Contact</a>
    </nav>
  </header>

  <section class="feature-band">
    <div class="feature-panel">
      <div class="news">
        <h1 class="news-title">Latest News</h1>

        <div class="post-head"><h2 class="post-title">Blog post title</h2><span class="post-date">2012/04/22</span></div>
        <div class="post-body">Pellentesque pharetra volutpat magna nec pulvinar. Sed laoreet, justo tempus gravida sagittis, ligula risus rutrum tellus, id tincid unt metus lorem vel mi. Vestibulum ante ipsum primis in faucibus orci luctus et ultrices posu ere cubilia Curae... <span class="read-more">[<a href="#">Read more</a>]</span></div>

        <div class="post-head"><h2 class="post-title">Blog post title</h2><span class="post-date">2012/04/22</span></div>
        <div class="post-body is-last">Pellentesque pharetra volutpat magna nec pulvinar. Sed laoreet, justo tempus gravida sagittis, ligula risus rutrum tellus, id tincid unt metus lorem vel mi. Vestibulum ante ipsum primis in faucibus orci luctus et ultrices posu ere cubilia Curae... <span class="read-more">[<a href="#">Read more</a>]</span></div>

        <a href="#" class="archive-link">Blog archive &raquo;</a>
      </div>

      <svg class="feature-art" viewBox="0 0 420 359" role="img" aria-label="Close-up photograph of brass clockwork gears, cropped into a diagonal triangle">
        <defs>
          <linearGradient id="gearTone" x1="0" y1="0" x2="1" y2="1">
            <stop offset="0" stop-color="var(--gold-dark)"/>
            <stop offset="0.35" stop-color="var(--gold)"/>
            <stop offset="0.7" stop-color="var(--gold-light)"/>
            <stop offset="1" stop-color="var(--gold)"/>
          </linearGradient>
        </defs>
        <polygon points="0,0 61,0 420,359 0,359" fill="url(#gearTone)"/>
      </svg>
    </div>
  </section>

  <footer class="site-footer">
    <div class="contact-block">
      <p><strong>Tanzeri Mechanics</strong><br>1180 Corvell Avenue, Suite 210<br>Riverton, PA 15990</p>
      <p>(555) 013-4472<br>Email: <a href="#">info@tanzerimechanics.example</a></p>
    </div>
    <div class="footer-brand">Tanzeri Mechanics</div>
    <div class="copyright">Content copyright 2012 &copy;<br>TANZERIMECHANICS.EXAMPLE<br>All rights reserved.</div>
  </footer>
</body>
</html>
```